ADA COMPLIANCE

We are in need of flyer or tri fold page for ada compliance, handicap ramps and parking lot striping.

Target Market(s)

Commercial Construction Industry

Industry/Entity Type

Parking

Font styles to use
Other font styles liked:
• Felix Titling

Colors
0355a3
acd036

Requirements
Must have
• Our Company Name and logo, 8004172593 number License #2837406
• List of services provided in uploaded images. Navy blue with high vizability green

```html
<!DOCTYPE html>
<html lang="en">
<head>
<meta charset="utf-8">
<title>Parking Lot Striping Flyer</title>
<link href="https://fonts.googleapis.com/css2?family=Lato:wght@400;700;900&display=swap" rel="stylesheet">
<style>
  :root {
    --navy: #1c2b5e;
    --navy-deep: #15224d;
    --green: #3cb54a;
    --paper: #ffffff;
    --header-top: #f2f2f2;
    --header-bottom: #d9d9d9;
    --stage: #e6e6e6;
    --ink: #1c2b5e;
  }
  html, body {
    margin: 0;
    padding: 0;
    width: 1200px;
    height: 800px;
    overflow: hidden;
    background: var(--stage);
    font-family: "Lato", Arial, sans-serif;
  }
  .flyer {
    position: absolute;
    left: 340px;
    top: 30px;
    width: 520px;
    height: 740px;
    background: var(--paper);
    box-shadow: 0 4px 18px rgba(0,0,0,0.25);
    overflow: hidden;
  }
  .flyer-header {
    height: 140px;
    background: linear-gradient(180deg, var(--header-top), var(--header-bottom));
    display: flex;
    align-items: center;
    justify-content: center;
  }
  .brand {
    display: flex;
    align-items: center;
    gap: 10px;
    color: var(--navy);
    font-weight: 700;
    font-size: 24px;
    letter-spacing: 1px;
  }
  .brand-mark {
    width: 18px;
    height: 18px;
    background: var(--navy);
    border-radius: 50%;
  }
  .photo-grid {
    background: var(--navy);
    padding: 6px;
    display: grid;
    grid-template-columns: 1.3fr 1fr 1fr 1fr;
    grid-template-rows: 170px 96px;
    gap: 5px;
  }
  .photo { display: block; }
  .photo-building { grid-column: 1 / 3; background: linear-gradient(160deg, #c9d4de, #8c8f8c 60%, #5c6155); }
  .photo-lot { grid-column: 3 / 5; background: linear-gradient(170deg, #9fc4e6, #2e4a8a 50%, #1d2c52); }
  .photo-entrance { background: linear-gradient(170deg, #b7aa92, #6b5d4c); }
  .photo-rail { background: linear-gradient(170deg, #c98a55, #4a4038); }
  .photo-court { background: linear-gradient(170deg, #b8c4c2, #6d7d7a); }
  .photo-floor { background: linear-gradient(170deg, #d7d7cf, #8a8a7c); }
  .details {
    padding: 16px 26px 0;
    color: var(--ink);
  }
  .details-title {
    margin: 0;
    font-size: 26px;
    font-weight: 900;
    color: var(--navy);
  }
  .details-intro {
    margin: 4px 0 10px;
    font-size: 15px;
  }
  .service-lists {
    display: flex;
    gap: 30px;
  }
  .service-list {
    list-style: none;
    margin: 0;
    padding: 0;
    font-size: 15px;
    line-height: 1.4;
  }
  .service-list li {
    display: flex;
    align-items: flex-start;
    gap: 8px;
  }
  .service-list .plain { padding-left: 0; }
  .tick {
    width: 15px;
    height: 15px;
    flex: none;
    margin-top: 3px;
  }
  .contact-band {
    position: absolute;
    left: 0;
    right: 0;
    bottom: 0;
    height: 86px;
    background: var(--navy-deep);
    border-top: 4px solid var(--green);
    text-align: center;
  }
  .call-us {
    margin: 10px 0 0;
    font-size: 38px;
    font-weight: 900;
    color: var(--green);
  }
  .license {
    margin: 2px 0 0;
    font-size: 13px;
    color: #ffffff;
  }
</style>
</head>
<body>
<article class="flyer">
  <header class="flyer-header">
    <div class="brand">
      <span class="brand-mark"></span>
      <span class="brand-name">KEYSTONE SITE SERVICES INC.</span>
    </div>
  </header>

  <section class="photo-grid">
    <div class="photo photo-building" role="img" aria-label="Concrete building with accessible ramps, stairs and railings"></div>
    <div class="photo photo-lot" role="img" aria-label="Freshly striped parking lot with blue handicap stalls and logos"></div>
    <div class="photo photo-entrance" role="img" aria-label="Garage entrance with No Parking pavement markings"></div>
    <div class="photo photo-rail" role="img" aria-label="Metal handrail along an accessible ramp"></div>
    <div class="photo photo-court" role="img" aria-label="Parking lot with fresh white line striping"></div>
    <div class="photo photo-floor" role="img" aria-label="Polished garage floor with yellow safety striping"></div>
  </section>

  <section class="details">
    <h1 class="details-title">Parking lot Striping : What exactly is It?</h1>
    <p class="details-intro">The application of traffic paint to:</p>
    <div class="service-lists">
      <ul class="service-list">
        <li><svg class="tick" viewBox="0 0 16 16"><rect width="16" height="16" rx="2" fill="#1c2b5e"/><path d="M3.5 8.5l3 3 6-7" fill="none" stroke="#fff" stroke-width="2"/></svg>Parking lot lines</li>
        <li><svg class="tick" viewBox="0 0 16 16"><rect width="16" height="16" rx="2" fill="#1c2b5e"/><path d="M3.5 8.5l3 3 6-7" fill="none" stroke="#fff" stroke-width="2"/></svg>Line striping &amp; stenciling</li>
        <li><svg class="tick" viewBox="0 0 16 16"><rect width="16" height="16" rx="2" fill="#1c2b5e"/><path d="M3.5 8.5l3 3 6-7" fill="none" stroke="#fff" stroke-width="2"/></svg>Curb Painting</li>
        <li><svg class="tick" viewBox="0 0 16 16"><rect width="16" height="16" rx="2" fill="#1c2b5e"/><path d="M3.5 8.5l3 3 6-7" fill="none" stroke="#fff" stroke-width="2"/></svg>Handicap Logos</li>
        <li><svg class="tick" viewBox="0 0 16 16"><rect width="16" height="16" rx="2" fill="#1c2b5e"/><path d="M3.5 8.5l3 3 6-7" fill="none" stroke="#fff" stroke-width="2"/></svg>Handicap ADA striping</li>
        <li><svg class="tick" viewBox="0 0 16 16"><rect width="16" height="16" rx="2" fill="#1c2b5e"/><path d="M3.5 8.5l3 3 6-7" fill="none" stroke="#fff" stroke-width="2"/></svg>Signs &amp; Poles</li>
        <li><svg class="tick" viewBox="0 0 16 16"><rect width="16" height="16" rx="2" fill="#1c2b5e"/><path d="M3.5 8.5l3 3 6-7" fill="none" stroke="#fff" stroke-width="2"/></svg>Fire Lanes and No Parking zones</li>
      </ul>
      <ul class="service-list">
        <li><svg class="tick" viewBox="0 0 16 16"><rect width="16" height="16" rx="2" fill="#1c2b5e"/><path d="M3.5 8.5l3 3 6-7" fill="none" stroke="#fff" stroke-width="2"/></svg>Car stops &amp; Bollards</li>
        <li><svg class="tick" viewBox="0 0 16 16"><rect width="16" height="16" rx="2" fill="#1c2b5e"/><path d="M3.5 8.5l3 3 6-7" fill="none" stroke="#fff" stroke-width="2"/></svg>Game Courts</li>
        <li><svg class="tick" viewBox="0 0 16 16"><rect width="16" height="16" rx="2" fill="#1c2b5e"/><path d="M3.5 8.5l3 3 6-7" fill="none" stroke="#fff" stroke-width="2"/></svg>Raised Pavement Markers</li>
        <li><svg class="tick" viewBox="0 0 16 16"><rect width="16" height="16" rx="2" fill="#1c2b5e"/><path d="M3.5 8.5l3 3 6-7" fill="none" stroke="#fff" stroke-width="2"/></svg>Thermoplastics</li>
        <li><svg class="tick" viewBox="0 0 16 16"><rect width="16" height="16" rx="2" fill="#1c2b5e"/><path d="M3.5 8.5l3 3 6-7" fill="none" stroke="#fff" stroke-width="2"/></svg>Pallet Striping</li>
        <li><svg class="tick" viewBox="0 0 16 16"><rect width="16" height="16" rx="2" fill="#1c2b5e"/><path d="M3.5 8.5l3 3 6-7" fill="none" stroke="#fff" stroke-width="2"/></svg>Pretty much any markings<br>on a parking lot area.</li>
      </ul>
    </div>
  </section>

  <footer class="contact-band">
    <p class="call-us">Call Us : 8004172593</p>
    <p class="license">License #2837406</p>
  </footer>
</article>
</body>
</html>
```